Norvel Hand Wash

Design hand washes. Total 12 variants to be designed.

Variants name are:

1) MILK &OLIVE
2) Shea Butter
3) Hidden Dawn
4) Cream and Peach
5) Milk and Honey
6) Amber Whisper
7) Bakhour
8) Musk
9) White Oud
10) Black Oud
11) Rose Oud
12) Oud & Sandalwood

Labels can be on transparent sticker or background colors. All variants will be differentiated by fragrances and color. Bottle will be transparent. Pumps used for dispensing will be in Black or Transparent Color.

Designers can initially present designs of 4-5 variants initially. Later based on feedback, they can work out on more.

Bottle is 400ml and shape is rectangle. Ignore the size on bottle picture. Bottle keyline is attached.

Target Market(s)

B+, B, C+

Requirements
Must have
• Some relation to the variant names

```html
<!DOCTYPE html>
<html lang="en">
<head>
<meta charset="utf-8">
<title>Norvel Hand Wash — Label Range</title>
<link rel="stylesheet" href="https://fonts.googleapis.com/css2?family=Montserrat:wght@200;300;500&family=Kaushan+Script&family=Great+Vibes&display=swap">
<style>
  :root{
    --bg:#c4c8cb;
    --ink:#ffffff;
    --olive-top:#80a21c; --olive-bottom:#698614; --olive-accent:#b8d84a;
    --amber-top:#b0700a; --amber-bottom:#9c5606; --amber-accent:#e2b21a;
    --peach-top:#e47c7a; --peach-bottom:#d8615f; --peach-accent:#f6b9a2;
    --dawn-top:#c42a3c; --dawn-bottom:#a81d2e; --dawn-accent:#f07a96;
    --honey-top:#e07610; --honey-bottom:#c85a06; --honey-accent:#f2b010;
    --shea-top:#c4aa0c; --shea-bottom:#a88806; --shea-accent:#ecdc1c;
  }
  *{margin:0;padding:0;box-sizing:border-box}
  html,body{width:1200px;height:1200px;overflow:hidden}
  body{background:var(--bg);position:relative;font-family:"Montserrat",sans-serif;color:var(--ink)}

  .label{
    position:absolute;width:180px;height:318px;border-radius:12px;overflow:hidden;
    background:linear-gradient(180deg,var(--top),var(--bottom));
    box-shadow:0 2px 6px rgba(0,0,0,.15);
  }
  .label--olive{left:258px;top:230px;--top:var(--olive-top);--bottom:var(--olive-bottom);--accent:var(--olive-accent)}
  .label--amber{left:479px;top:230px;--top:var(--amber-top);--bottom:var(--amber-bottom);--accent:var(--amber-accent)}
  .label--peach{left:706px;top:230px;--top:var(--peach-top);--bottom:var(--peach-bottom);--accent:var(--peach-accent)}
  .label--dawn{left:254px;top:764px;--top:var(--dawn-top);--bottom:var(--dawn-bottom);--accent:var(--dawn-accent)}
  .label--honey{left:482px;top:764px;--top:var(--honey-top);--bottom:var(--honey-bottom);--accent:var(--honey-accent)}
  .label--shea{left:706px;top:764px;--top:var(--shea-top);--bottom:var(--shea-bottom);--accent:var(--shea-accent)}

  .texture{
    position:absolute;inset:0;
    background:radial-gradient(circle at 40% 45%,rgba(255,255,255,.10),rgba(255,255,255,0) 60%);
  }

  .brand{
    position:absolute;top:28px;left:0;width:100%;text-align:center;
    font-weight:500;font-size:19px;letter-spacing:.5px;
  }
  .name{position:absolute;left:0;width:100%;text-align:center;line-height:1;white-space:nowrap}
  .name__thin{font-weight:200;font-size:48px}
  .name__amp{font-family:"Great Vibes",cursive;font-size:90px;color:var(--accent);opacity:.8}
  .name__script{font-family:"Kaushan Script",cursive;font-size:46px}
  .name__sub{font-weight:200;font-size:36px}
  .volume{position:absolute;left:110px;top:245px;font-weight:300;font-size:10.5px}
</style>
</head>
<body>

<div class="label label--olive">
  <div class="texture" role="img" aria-label="Soft light bubble pattern"></div>
  <div class="brand">Norvel</div>
  <div class="name name__thin" style="top:96px">milk</div>
  <div class="name name__amp" style="top:112px">&amp;</div>
  <div class="name name__thin" style="top:176px">olive</div>
  <div class="volume">400 ml</div>
</div>

<div class="label label--amber">
  <div class="texture" role="img" aria-label="Soft light bubble pattern"></div>
  <div class="brand">Norvel</div>
  <div class="name name__script" style="top:120px">amber</div>
  <div class="name name__sub" style="top:176px">whisper</div>
  <div class="volume">400 ml</div>
</div>

<div class="label label--peach">
  <div class="texture" role="img" aria-label="Soft light bubble pattern"></div>
  <div class="brand">Norvel</div>
  <div class="name name__thin" style="top:110px">cream</div>
  <div class="name name__amp" style="top:122px">&amp;</div>
  <div class="name name__thin" style="top:180px">peach</div>
  <div class="volume">400 ml</div>
</div>

<div class="label label--dawn">
  <div class="texture" role="img" aria-label="Soft light bubble pattern"></div>
  <div class="brand">Norvel</div>
  <div class="name name__script" style="top:118px">hidden</div>
  <div class="name name__sub" style="top:170px">dawn</div>
  <div class="volume">400 ml</div>
</div>

<div class="label label--honey">
  <div class="texture" role="img" aria-label="Soft light bubble pattern"></div>
  <div class="brand">Norvel</div>
  <div class="name name__thin" style="top:96px">milk</div>
  <div class="name name__amp" style="top:116px">&amp;</div>
  <div class="name name__thin" style="top:180px">honey</div>
  <div class="volume">400 ml</div>
</div>

<div class="label label--shea">
  <div class="texture" role="img" aria-label="Soft light bubble pattern"></div>
  <div class="brand">Norvel</div>
  <div class="name name__script" style="top:120px">shea</div>
  <div class="name name__sub" style="top:174px">butter</div>
  <div class="volume">400 ml</div>
</div>

</body>
</html>
```